PDN Letterhead

We need a letterhead design that will be able to be used on all marketing products (letterhead, mail chimp, envelops, business cards, etc.) We are a law firm specializing primarily in transportation law but offer a wide range of services to our clients. We would like the design to be modern, simple, and professional. Our colors are black and gold, however, we've incorporated dark gray and white on other marketing products such as our website.

```html
<!DOCTYPE html>
<html lang="en">
<head>
<meta charset="utf-8">
<title>PDN Law Group Letterhead</title>
<link rel="stylesheet" href="https://fonts.googleapis.com/css2?family=Source+Sans+3:wght@400;700&display=swap">
<style>
  :root {
    --backdrop: #b3b3b3;
    --paper: #ffffff;
    --ink: #5c5c5c;
    --ink-dark: #2b2b2b;
    --rule: #4a4a4a;
    --gold: #a8895c;
    --icon: #1f6fc2;
    --sig-tone: #e6e6e6;
  }
  * { box-sizing: border-box; margin: 0; padding: 0; }
  html, body {
    width: 1012px; height: 1200px; overflow: hidden;
    background: var(--backdrop);
    font-family: "Source Sans 3", "Myriad Pro", Arial, sans-serif;
  }
  .sheet {
    position: absolute; left: 82px; top: 77px;
    width: 848px; height: 1034px;
    background: var(--paper);
  }
  .brand {
    position: absolute; top: 82px; left: 0; width: 100%;
    text-align: center;
    font-weight: 400; font-size: 27px; letter-spacing: 2px;
    color: var(--ink-dark);
  }
  .rule {
    position: absolute; height: 1px; background: var(--rule);
  }
  .rule--top { top: 170px; left: 72px; width: 692px; }
  .rule--bottom { top: 949px; left: 77px; width: 692px; background: #777; }
  .letter-body {
    position: absolute; top: 211px; left: 87px; width: 686px;
    color: var(--ink); font-size: 14.6px; line-height: 19px;
    text-align: justify;
  }
  .letter-body p + p { margin-top: 19px; }
  .signature-mark {
    position: absolute; top: 855px; left: 600px;
    width: 139px; height: 30px; background: var(--sig-tone);
    border-radius: 3px;
  }
  .signatory {
    position: absolute; top: 891px; left: 600px; width: 178px;
    text-align: center; color: var(--ink); font-size: 14.6px;
    transform: translateX(-31px);
  }
  .contact-bar {
    position: absolute; top: 972px; left: 84px; width: 690px;
    display: flex; justify-content: space-between; align-items: flex-start;
    font-size: 10.6px; font-weight: 700; color: var(--ink-dark); line-height: 13.5px;
  }
  .contact-item { display: flex; align-items: flex-start; gap: 6px; }
  .contact-item svg { flex: none; margin-top: 2px; fill: var(--icon); }
  .contact-item--inline { margin-top: 2px; }
</style>
</head>
<body>
  <main class="sheet">
    <div class="brand">PDN Law Group</div>
    <div class="rule rule--top"></div>

    <section class="letter-body">
      <p>Lorem ipsum dolor sit amet, consectetur adipiscing elit, sed do eiusmod tempor incididunt ut labore et dolore magna aliqua. Ut enim ad minim veniam, quis nostrud exercitation ullamco laboris nisi ut aliquip ex ea commodo consequat. Duis aute irure dolor in reprehenderit in voluptate velit esse cillum dolore eu fugiat nulla pariatur. Excepteur sint occaecat cupidatat non proident, sunt in culpa qui officia deserunt mollit anim id est laborum</p>
      <p>Sed ut perspiciatis unde omnis iste natus error sit voluptatem accusantium doloremque laudantium, totam rem aperiam, eaque ipsa quae ab illo inventore veritatis et quasi architecto beatae vitae dicta sunt explicabo. Nemo enim ipsam voluptatem quia voluptas sit aspernatur aut odit aut fugit, sed quia consequuntur magni dolores eos qui ratione voluptatem sequi nesciunt. Neque porro quisquam est, qui dolorem ipsum quia dolor sit amet, consectetur, adipisci velit, sed quia non numquam eius modi tempora incidunt ut labore et dolore magnam aliquam quaerat voluptatem. Ut enim ad minima veniam, quis nostrum exercitationem ullam corporis suscipit laboriosam, nisi ut aliquid ex ea commodi consequatur? Quis autem vel eum iure reprehenderit qui in ea voluptate velit esse quam nihil molestiae consequatur, vel illum qui dolorem eum fugiat quo voluptas nulla pariatur?</p>
      <p>Lorem ipsum dolor sit amet, consectetur adipiscing elit, sed do eiusmod tempor incididunt ut labore et dolore magna aliqua. Ut enim ad minim veniam, quis nostrud exercitation ullamco laboris nisi ut aliquip ex ea commodo consequat. Duis aute irure dolor in reprehenderit in voluptate velit esse cillum dolore eu fugiat nulla pariatur. Excepteur sint occaecat cupidatat non proident, sunt in culpa qui officia deserunt mollit anim id est laborum</p>
      <p>Sed ut perspiciatis unde omnis iste natus error sit voluptatem accusantium doloremque laudantium, totam rem aperiam, eaque ipsa quae ab illo inventore veritatis et quasi architecto beatae vitae dicta sunt explicabo. Nemo enim ipsam voluptatem quia voluptas sit aspernatur aut odit aut fugit, sed quia consequuntur magni dolores eos qui ratione voluptatem sequi nesciunt. Neque porro quisquam est, qui dolorem ipsum quia dolor sit amet, consectetur, adipisci velit, sed quia non numquam eius modi tempora incidunt ut labore et dolore magnam aliquam quaerat voluptatem. Ut enim ad minima veniam, quis nostrum exercitationem ullam corporis suscipit laboriosam, nisi ut aliquid ex ea commodi consequatur? Quis autem vel eum iure reprehenderit qui in ea voluptate velit esse quam nihil molestiae consequatur, vel illum qui dolorem eum fugiat quo voluptas nulla pariatur?</p>
    </section>

    <div class="signature-mark" role="img" aria-label="Handwritten signature"></div>
    <div class="signatory">Name Name</div>

    <div class="rule rule--bottom"></div>

    <footer class="contact-bar">
      <div class="contact-item">
        <svg width="9" height="12" viewBox="0 0 9 12" aria-hidden="true"><path d="M4.5 0A4.5 4.5 0 0 0 0 4.5C0 7.8 4.5 12 4.5 12S9 7.8 9 4.5A4.5 4.5 0 0 0 4.5 0zm0 6.3a1.8 1.8 0 1 1 0-3.6 1.8 1.8 0 0 1 0 3.6z"/></svg>
        <span>220 Harbor Crest Avenue,<br>Suite 300, Portview, FL 33990</span>
      </div>
      <div class="contact-item contact-item--inline">
        <svg width="10" height="10" viewBox="0 0 10 10" aria-hidden="true"><path d="M2 0.4 3.6 2.6 2.7 3.8C3.3 5.2 4.8 6.7 6.2 7.3L7.4 6.4 9.6 8 8.6 9.6C4.6 9.6 0.4 5.4 0.4 1.4z"/></svg>
        <span>555.014.2290</span>
      </div>
      <div class="contact-item contact-item--inline">
        <svg width="11" height="9" viewBox="0 0 11 9" aria-hidden="true"><path d="M0 1h11v1L5.5 5 0 2zM0 3.2l5.5 3 5.5-3V8H0z"/></svg>
        <span>admin@pdnlawgroup.com</span>
      </div>
      <div class="contact-item contact-item--inline">
        <svg width="10" height="10" viewBox="0 0 10 10" aria-hidden="true"><circle cx="5" cy="5" r="4.6"/><path d="M0.6 5h8.8M5 0.5v9M5 0.5C2.5 3 2.5 7 5 9.5M5 0.5C7.5 3 7.5 7 5 9.5" stroke="#fff" stroke-width="0.7" fill="none"/></svg>
        <span>www.pdnlawgroup.com</span>
      </div>
    </footer>
  </main>
</body>
</html>
```